Web Design for Webdesign company 3 page PSD

Project
---------
We need a PSD Web Design to be used in a WordPress installation.
What we would like to create is a professional looking website for a web design agency. We also need you to look for suitable stock images to be placed on these pages.
We need the design for:
Homepage
Landing page
Contact page
attached in the pages file you will find a file with more in depth details how these files should be build up.
We would like to see a desktop version and a mobile version of these pages
The website should have a 1100px width.
The mobile design should have 480px width.
The homepage should have a header slider about 450px high.
The slider is preferred full width and should have some images text and a button
Objectives
-------------
The main objective for the website is to get leads from customers in the form of a request for a quotation or a call or mail me back action. The most important action for the homepage is to link and navigate to our landing pages.
What we want to tell our visitors (our main products)
-------------------------------------------------------------------
- A website with no big investment but a monthly rate
- A successful website with no worries (a complete website, seo, hosting and a service contract for future customization is included for a monthly rate)
Color Scheme
------------
Use branding colors. You can find them in the branding.pdf file.
Additional colors:
White: #ffffff
Black: #181818
Company info
--------------
We are a starting web design / marketing agency based in The Netherlands and looking for the design of our website. Our services are (custom) webdesign, website marketing or combinations of both. Our main customer group is small business owners.
We sell websites but give the option to buy it with a lease contract.
A second product is a default website with a complete service: SEO, hosting and a service contract for a monthly rate.
Content:
-----------
If not available place Lorem Ipsum text.
There will come about 400 words of text on the landing pages
Design Competition
--------------------------
Since this is a designing competition we would like to see your creativity.
What you can expect from us is a lot of feedback 7 days a week with short response time.
You can send us the first sketchy mock ups of the homepage and we will give feedback based on these design. But we like your feedback or comments as well
Read the pages file for more in depth details how the pages should be designed

Target Market(s)
Small business owners in The Netherlands
Industry/Entity Type
It Company
Number of Pages Required
3 page
Requirements
Must have
- Homepage:
- Header slider with images, some text and a link to a custom page
- The slider should have 3 designed slides
- Landings page:
- Sidebar
- Action button for a request for a quotation
- Action button for a call me back action
- Action button for an appointment
- Contact form:
- Address details
- Contact form
Nice to have
- Homepage:
- Full width slider
- Testimonial block
- Blog items
Should not have
- Flash
- A to crowded design

```html
<!DOCTYPE html>
<html lang="en">
<head>
<meta charset="utf-8">
<title>Rising Oak – Web Design</title>
<link href="https://fonts.googleapis.com/css2?family=Arimo:wght@400;700&family=Open+Sans:ital,wght@0,400;0,600;0,700;1,400&display=swap" rel="stylesheet">
<style>
  :root{
    --green:#4f8a6d;
    --green-dark:#3f7a5d;
    --teal:#2a6e7c;
    --ink:#181818;
    --text:#444444;
    --muted:#777777;
    --white:#ffffff;
    --panel:#f2f2f2;
    --line:#dddddd;
    --footer:#333333;
    --footer-base:#262626;
    --footer-text:#bbbbbb;
    --nav:#555555;
  }
  *{margin:0;padding:0;box-sizing:border-box}
  html,body{width:675px;height:1200px;overflow:hidden;background:var(--white)}
  body{position:relative;font-family:"Open Sans",Arial,sans-serif;color:var(--text)}
  .abs{position:absolute}
  .heading{font-family:"Arimo",Arial,sans-serif;font-weight:700;color:var(--ink)}

  /* header */
  .site-header{left:0;top:0;width:675px;height:62px;background:var(--white)}
  .brand{left:52px;top:18px;display:flex;align-items:center;gap:8px}
  .brand-dot{width:24px;height:24px;border-radius:50%;background:var(--green);display:block}
  .brand-name{font-family:"Arimo",Arial,sans-serif;font-weight:700;font-size:14px;color:var(--ink);letter-spacing:.3px}
  .nav-item{top:23px;height:17px;font-family:"Arimo",Arial,sans-serif;font-weight:700;font-size:8px;color:var(--nav);line-height:17px;letter-spacing:.4px;text-align:center}
  .nav-item.active{background:var(--nav);color:var(--white);border-radius:9px}

  /* hero */
  .hero{left:0;top:62px;width:675px;height:233px;background:radial-gradient(ellipse at 50% 45%,#a3c5b0 0%,#7fb092 35%,#5e9a77 75%,#4f8c69 100%)}
  .hero-title{top:12px;left:0;width:675px;text-align:center;font-family:"Arimo",Arial,sans-serif;font-weight:700;font-size:25.5px;color:var(--white);letter-spacing:.4px}
  .hero-sub{top:43px;left:0;width:675px;text-align:center;font-family:"Arimo",Arial,sans-serif;font-weight:700;font-size:10px;color:var(--white);letter-spacing:.2px}
  .hero-devices{left:140px;top:73px;width:345px;height:155px;border-radius:6px;background:linear-gradient(180deg,#e9ecea 0%,#cfd5d2 60%,#b9c1bd 100%)}
  .hero-arrow{top:92px}
  .btn-pill{left:502px;top:188px;width:112px;height:20px;border-radius:10px;background:var(--white);font-family:"Arimo",Arial,sans-serif;font-weight:700;font-size:8px;color:var(--ink);text-align:center;line-height:20px;letter-spacing:.3px}

  /* services */
  .service-card{top:316px;width:177px;height:108px;overflow:hidden}
  .service-photo{position:absolute;inset:0}
  .service-label{position:absolute;left:10px;bottom:8px;font-family:"Arimo",Arial,sans-serif;font-weight:400;font-size:10px;color:var(--white);letter-spacing:.2px}
  .service-go{position:absolute;right:9px;bottom:8px}

  .intro{top:447px;left:145px;width:385px;text-align:center;font-family:"Arimo",Arial,sans-serif;font-weight:700;font-size:11.5px;line-height:15px;color:var(--ink)}
  .btn-quote{left:273px;top:489px;width:129px;height:32px;background:var(--green);border-radius:2px;box-shadow:0 2px 0 var(--green-dark);display:flex;align-items:center;justify-content:center;gap:6px;font-family:"Arimo",Arial,sans-serif;font-size:12.5px;color:var(--white);letter-spacing:.3px}

  /* welcome */
  .welcome-title{left:52px;top:563px;font-size:13px;letter-spacing:.2px}
  .welcome-title span{color:var(--teal)}
  .welcome-copy{left:52px;top:587px;width:326px;font-size:7.2px;line-height:12.3px;color:var(--text)}
  .welcome-copy p+p{margin-top:9px}
  .btn-lease{left:52px;top:687px;width:96px;height:23px;background:var(--green);border-radius:2px;color:var(--white);font-family:"Arimo",Arial,sans-serif;font-weight:700;font-size:8px;text-align:center;line-height:23px;letter-spacing:.3px}
  .welcome-photo{left:396px;top:566px;width:227px;height:155px;background:linear-gradient(160deg,#3b4152 0%,#6d6f78 45%,#d8d6d2 75%,#f2f0ec 100%)}

  /* testimonials + blog */
  .panel{left:0;top:752px;width:675px;height:238px;background:var(--panel);border-top:1px solid #e4e4e4}
  .panel-title{font-size:13px;font-weight:400;font-family:"Arimo",Arial,sans-serif;color:var(--ink)}
  .dots{left:296px;top:786px;display:flex;gap:3px}
  .dots i{width:5px;height:5px;border-radius:50%;background:#d3d3d3;display:block}
  .dots i:first-child{background:#aaa}
  .quote-box{left:52px;top:803px;width:278px;height:103px;background:var(--white);box-shadow:0 1px 3px rgba(0,0,0,.12);padding:16px 15px;font-size:7.2px;line-height:12.3px;color:var(--text)}
  .quote-tail{left:64px;top:905px}
  .avatar{left:52px;top:924px;width:40px;height:40px;border:2px solid var(--white);box-shadow:0 0 2px rgba(0,0,0,.2);background:linear-gradient(180deg,#c9a88c 0%,#8a6a55 60%,#5f4e44 100%)}
  .client-name{left:102px;top:933px;font-family:"Arimo",Arial,sans-serif;font-weight:700;font-size:8.5px;color:var(--ink)}
  .client-role{left:102px;top:945px;font-size:6px;color:var(--muted)}

  .post{left:345px;width:278px;height:46px}
  .post-date{position:absolute;left:0;top:0;width:30px;height:34px;background:var(--white);box-shadow:0 1px 2px rgba(0,0,0,.2);text-align:center}
  .post-date .m{display:block;height:10px;background:var(--green);color:var(--white);font-family:"Arimo",Arial,sans-serif;font-weight:700;font-size:7px;line-height:10px}
  .post-date .d{display:block;font-family:"Arimo",Arial,sans-serif;font-weight:700;font-size:11px;line-height:12px;color:var(--ink)}
  .post-date .y{display:block;font-size:6px;line-height:8px;color:var(--ink)}
  .post-title{position:absolute;left:37px;top:1px;font-family:"Arimo",Arial,sans-serif;font-weight:700;font-size:8.5px;color:var(--ink)}
  .post-text{position:absolute;left:37px;top:17px;width:228px;font-size:6.6px;line-height:9.5px;color:var(--text)}
  .post-text b{font-weight:400;color:var(--green)}
  .post-rule{left:345px;width:278px;height:1px;background:var(--line)}

  /* footer */
  .footer{left:0;top:990px;width:675px;height:170px;background:var(--footer)}
  .f-title{font-family:"Arimo",Arial,sans-serif;font-weight:700;font-size:8px;color:var(--white);line-height:11px;letter-spacing:.2px}
  .f-input{left:52px;width:136px;height:18px;background:var(--white);border-radius:2px;font-size:6.5px;color:#999;padding-left:5px;line-height:18px}
  .f-btn{left:52px;top:1103px;width:136px;height:17px;background:var(--green);border-radius:2px;font-family:"Arimo",Arial,sans-serif;font-weight:700;font-size:7.5px;color:var(--white);text-align:center;line-height:17px}
  .f-links{left:228px;top:1038px;list-style:none}
  .f-links li{font-size:7px;line-height:13.6px;color:var(--footer-text)}
  .f-contact{left:344px;font-size:7px;line-height:10.5px;color:var(--footer-text);padding-left:15px}
  .f-contact svg{position:absolute;left:0;top:1px}
  .f-social{left:497px;font-size:7px;color:var(--footer-text);display:flex;align-items:center;gap:6px}
  .f-social i{width:14px;height:14px;border:1px solid var(--footer-text);border-radius:50%;display:block}
  .base{left:0;top:1160px;width:675px;height:40px;background:var(--footer-base);text-align:center;padding-top:8px;font-size:7px;line-height:12.5px;color:var(--footer-text)}
</style>
</head>
<body>

<header class="abs site-header">
  <div class="abs brand">
    <span class="brand-dot"></span>
    <span class="brand-name">RISING OAK</span>
  </div>
  <nav>
    <a class="abs nav-item active" style="left:321px;width:46px">HOME</a>
    <a class="abs nav-item" style="left:376px;width:50px">LANDING</a>
    <a class="abs nav-item" style="left:441px;width:72px">TESTIMONIALS</a>
    <a class="abs nav-item" style="left:528px;width:34px">BLOG</a>
    <a class="abs nav-item" style="left:576px;width:52px">CONTACT</a>
  </nav>
</header>

<section class="abs hero">
  <h1 class="abs hero-title">RESPONSIVE WEB DESIGN</h1>
  <p class="abs hero-sub">YOUR WEBSITE READABLE ON ALL DEVICES</p>
  <svg class="abs" style="left:455px;top:22px" width="70" height="52" viewBox="0 0 70 52">
    <path d="M50 2 C62 6 62 20 50 24 C38 28 36 40 42 50" fill="none" stroke="#fff" stroke-width="1" stroke-dasharray="2 2"/>
    <path d="M38 46 L42 50 L45 45" fill="none" stroke="#fff" stroke-width="1"/>
  </svg>
  <div class="abs hero-devices" role="img" aria-label="Tablet, desktop monitor and smartphone showing a responsive website layout"></div>
  <svg class="abs hero-arrow" style="left:50px" width="14" height="50" viewBox="0 0 14 50"><path d="M12 1 L2 25 L12 49" fill="none" stroke="#fff" stroke-width="1"/></svg>
  <svg class="abs hero-arrow" style="left:611px" width="14" height="50" viewBox="0 0 14 50"><path d="M2 1 L12 25 L2 49" fill="none" stroke="#fff" stroke-width="1"/></svg>
  <div class="abs btn-pill">MORE INFORMATION</div>
</section>

<article class="abs service-card" style="left:52px">
  <div class="service-photo" role="img" aria-label="Business team meeting around a table in a bright office" style="background:linear-gradient(180deg,#d8dde2 0%,#8a8f99 55%,#3c4150 100%)"></div>
  <span class="service-label">WEB DESIGN</span>
  <svg class="service-go" width="11" height="11" viewBox="0 0 11 11"><circle cx="5.5" cy="5.5" r="5.5" fill="#fff"/><path d="M4.5 3 L7 5.5 L4.5 8" fill="none" stroke="#222" stroke-width="1.3"/></svg>
</article>
<article class="abs service-card" style="left:249px">
  <div class="service-photo" role="img" aria-label="Two businessmen reviewing documents together" style="background:linear-gradient(180deg,#9aa0a8 0%,#5c6470 50%,#2b3140 100%)"></div>
  <span class="service-label">WEBSITE RENT</span>
  <svg class="service-go" width="11" height="11" viewBox="0 0 11 11"><circle cx="5.5" cy="5.5" r="5.5" fill="#fff"/><path d="M4.5 3 L7 5.5 L4.5 8" fill="none" stroke="#222" stroke-width="1.3"/></svg>
</article>
<article class="abs service-card" style="left:446px">
  <div class="service-photo" role="img" aria-label="Hand touching a glowing digital search network interface" style="background:linear-gradient(160deg,#0f2a3a 0%,#1f5272 50%,#0b1a26 100%)"></div>
  <span class="service-label">SEO</span>
  <svg class="service-go" width="11" height="11" viewBox="0 0 11 11"><circle cx="5.5" cy="5.5" r="5.5" fill="#fff"/><path d="M4.5 3 L7 5.5 L4.5 8" fill="none" stroke="#222" stroke-width="1.3"/></svg>
</article>

<p class="abs intro">A handy Lorem Ipsum Generator that helps to create dummy text for all layout needs.</p>
<div class="abs btn-quote">GET A QUOTE
  <svg width="16" height="16" viewBox="0 0 16 16"><circle cx="8" cy="8" r="7" fill="none" stroke="#fff" stroke-width="1.5"/><path d="M7 4.8 L10 8 L7 11.2" fill="none" stroke="#fff" stroke-width="1.6"/></svg>
</div>

<h2 class="abs heading welcome-title">WELCOME TO <span>RISING OAK</span></h2>
<div class="abs welcome-copy">
  <p>Lorem ipsum dolor sit amet, cu per augue graeco cotidieque. Est ut novum laudem definiebas, no augue necessitatibus nam. Te erant dissentias appellantur cum, errem mentitum conceptam ad eum. Ad has meis adipisci, eu sed iracundia reprimique, eius perpetua vis te. Fuisset democritum scribentur ex est, mei ei viderer sapientem suscipiantur.</p>
  <p>Euismod appareat explicari et quo. Mei in natum errem scribentur, idque affert abhorreant et pri, ex eum torquatos adolescens. Erroribus conclusionemque cu quo. Novum putent his eu.</p>
</div>
<div class="abs btn-lease">LEASE CONTRACT</div>
<div class="abs welcome-photo" role="img" aria-label="Hand in a suit signing a contract with a pen"></div>

<section class="abs panel"></section>
<h3 class="abs panel-title" style="left:52px;top:780px">Client Testimonials</h3>
<div class="abs dots"><i></i><i></i><i></i><i></i><i></i></div>
<blockquote class="abs quote-box">"Lorem ipsum dolor sit amet, cu per augue graeco cotidieque. Est ut novum laudem definiebas, no augue necessitatibus nam. Te erant dissentias appellantur cum, errem mentitum conceptam ad eum. Ad has meis adipisci, eu sed iracundia reprimique, eius perpetua vis te. Fuisset democritum scribentur ex est, mei ei viderer sapientem suscipiantur."</blockquote>
<svg class="abs quote-tail" width="16" height="8" viewBox="0 0 16 8"><path d="M0 0 L8 8 L16 0Z" fill="#fff"/></svg>
<div class="abs avatar" role="img" aria-label="Portrait photo of the client"></div>
<div class="abs client-name">Marla Vendig,</div>
<div class="abs client-role">(lorem ipsum dolor amet)</div>

<h3 class="abs panel-title" style="left:345px;top:779px">Latest Blog</h3>
<article class="abs post" style="top:804px">
  <div class="post-date"><span class="m">FEB</span><span class="d">01</span><span class="y">2014</span></div>
  <div class="post-title">Lorem ipsum dolor sit amet...</div>
  <p class="post-text">Lorem Ipsum is simply dummy text of the printing and typesetting industry. <b>[+]</b></p>
</article>
<div class="abs post-rule" style="top:853px"></div>
<article class="abs post" style="top:866px">
  <div class="post-date"><span class="m">FEB</span><span class="d">01</span><span class="y">2014</span></div>
  <div class="post-title">Lorem ipsum dolor sit amet...</div>
  <p class="post-text">Lorem Ipsum is simply dummy text of the printing and typesetting industry. <b>[+]</b></p>
</article>
<div class="abs post-rule" style="top:915px"></div>
<article class="abs post" style="top:929px">
  <div class="post-date"><span class="m">FEB</span><span class="d">01</span><span class="y">2014</span></div>
  <div class="post-title">Lorem ipsum dolor sit amet...</div>
  <p class="post-text">Lorem Ipsum is simply dummy text of the printing and typesetting industry. <b>[+]</b></p>
</article>

<footer class="abs footer"></footer>
<div class="abs f-title" style="left:52px;top:1020px">SUBSCRIBE TO<br>OUR NEWSLETTER</div>
<div class="abs f-input" style="top:1056px">Enter Your Name</div>
<div class="abs f-input" style="top:1079px">Enter Your Email</div>
<div class="abs f-btn">SUBSCRIBE</div>

<div class="abs f-title" style="left:228px;top:1020px">QUICK LINKS</div>
<ul class="abs f-links"><li>Home</li><li>Landing</li><li>Testimonials</li><li>Blog</li><li>Contact</li></ul>

<div class="abs f-title" style="left:344px;top:1020px">CONTACT INFO</div>
<div class="abs f-contact" style="top:1040px">
  <svg width="7" height="9" viewBox="0 0 7 9"><path d="M3.5 0 A3.5 3.5 0 0 1 7 3.5 C7 6 3.5 9 3.5 9 C3.5 9 0 6 0 3.5 A3.5 3.5 0 0 1 3.5 0Z" fill="#bbb"/><circle cx="3.5" cy="3.5" r="1.3" fill="#333"/></svg>
  228, lorem ipsum dolor sit,<br>dosis miunf- 845848
</div>
<div class="abs f-contact" style="top:1072px">
  <svg width="8" height="8" viewBox="0 0 8 8"><path d="M1 0.5 L3 0.5 L3.6 2.5 L2.5 3.3 C3 4.5 3.6 5 4.7 5.5 L5.5 4.4 L7.5 5 L7.5 7 C4 7.5 0.5 4 1 0.5Z" fill="#bbb"/></svg>
  Phone: (800)555-01-2233<br>Fax: (800)555-01-2244
</div>
<div class="abs f-contact" style="top:1102px">
  <svg width="8" height="7" viewBox="0 0 8 7"><path d="M0.5 3 L4 0.5 L7.5 3 L7.5 6.5 L0.5 6.5Z" fill="none" stroke="#bbb"/><path d="M0.5 3 L4 5 L7.5 3" fill="none" stroke="#bbb"/></svg>
  Email: info@risingoak.example<br>Website:www.risingoak.example
</div>

<div class="abs f-title" style="left:497px;top:1020px">STAY CONNECTED</div>
<div class="abs f-social" style="top:1039px"><i></i>Follow Us On Facelink</div>
<div class="abs f-social" style="top:1065px"><i></i>Follow Us On Chirper</div>
<div class="abs f-social" style="top:1092px"><i></i>Follow Us On WorkNet</div>

<div class="abs base">© 2015 Rising Oak All Rights Reserved.<br>Terms of Use | Legal Disclaimer | Privacy Policy | References</div>

</body>
</html>
```